CareWillow Brand Standards and Core Values

I would like to have frameable posters made up for each office using our brand standards. I would like the posters to include:Our Vision Statement:We are transforming the healthcare staffing and homecare industry with our people-oriented, world-class team. Clients choose us, and develop lasting bonds with our team because of our impeccably high standards and our reputation for always remembering this is, first and foremost, a people business. We consistently go the extra mile to ensure our nurses and those being cared for are at all times, treated with dignity and respect. We hold ourselves and those we work with to the highest possible standards. We consistently deliver what we promise, and whenever possible, even more. Our Mission Statement:We go above and beyond to ensure our clients receive the right care and the right people at the right time. Our rigorous recruitment standards result in strong caregivers who are trusted for their expertise, experience and compassion. Our Values:Through our genuine caring and compassion, we are committed to honor all with whom we interact. We are grounded in our faith and dedicated to working together as a family that consistently and passionately lives our values. Compassion Integrity and honesty Faith Decisive action Constant and never-ending improvement Personal ownership Excellence Positive attitude Passion RespectWho we are:We are friendly, servant leaders who have a sense of urgency to meet the needs of our nurses and clients. We prioritize personal relationships with genuine caring and compassion. We inspire others through our passion and energy.Our main colors are: HEX# 5C80DE, HEX# BDE080, HEX# 8C8C8Caccent colors are: HEX# 95D6E3, HEX# AD59AB, HEX# 002E57

Target Market(s)

office employee inspiration

Font styles to use
Other font styles liked:
• Verdana

Colors

Designer to choose colors to be used in the design.

Requirements
Must have
• the core values listed in description
Nice to have
• colors given in description, something fun and inspiring for office employees to help motivate them !
Should not have
• colors that are not company colors. I have listed HEX codes in description

```html
<!DOCTYPE html>
<html lang="en">
<head>
<meta charset="utf-8">
<title>CareWillow Core Values Poster</title>
<link href="https://fonts.googleapis.com/css2?family=Montserrat:wght@400;500;600;700;900&display=swap" rel="stylesheet">
<style>
  :root {
    --brand-blue: #5c80de;
    --heading-blue: #4a6fd8;
    --brand-lime: #bde080;
    --brand-teal: #33ccb5;
    --soft-teal: #95d6e3;
    --navy: #002e57;
    --body-grey: #555a60;
    --panel-white: #ffffff;
    --panel-grey: #f0f0f0;
    --panel-light: #f7f7f7;
    --page-bg: #ffffff;
  }
  * { box-sizing: border-box; margin: 0; padding: 0; }
  html, body {
    width: 703px; height: 1200px; overflow: hidden;
    background: var(--page-bg);
    font-family: "Montserrat", Verdana, sans-serif;
  }
  .poster {
    position: absolute; left: 23px; top: 137px;
    width: 576px; height: 813px;
    transform: scale(1.14); transform-origin: top left;
    background: var(--brand-blue);
    overflow: hidden;
    box-shadow: 8px 10px 24px rgba(0,0,0,0.25);
  }
  .headline { position: absolute; left: 28px; top: 36px; color: #fff; }
  .headline .line-lg { font-size: 30px; font-weight: 400; letter-spacing: 0.5px; line-height: 1; }
  .headline .line-sm { font-size: 20.5px; font-weight: 400; line-height: 1; margin-top: 4px; }
  .headline .word-health { font-size: 56px; font-weight: 900; color: var(--brand-teal); line-height: 0.98; margin-top: 6px; letter-spacing: 1px; }
  .headline .word-care { font-size: 82px; font-weight: 900; color: var(--brand-lime); line-height: 0.88; letter-spacing: 1px; }

  .brand { position: absolute; left: 308px; top: 48px; width: 245px; display: flex; align-items: center; gap: 12px; color: #fff; }
  .brand-dot { width: 30px; height: 30px; border-radius: 50%; border: 2px solid #fff; flex: none; }
  .brand-name { font-size: 22px; font-weight: 500; line-height: 1; }

  .who-tag {
    position: absolute; left: 0; top: 260px; width: 158px; height: 20px;
    background: var(--brand-lime); border-radius: 0 10px 10px 0;
    color: #2d3a20; font-weight: 700; font-size: 14px; line-height: 20px; padding-left: 33px;
  }
  .who-text {
    position: absolute; left: 34px; top: 298px; width: 238px;
    color: #fff; font-size: 10.2px; line-height: 1.26; text-align: justify; font-weight: 400;
  }

  .photo {
    position: absolute; left: 0; top: 385px; width: 330px; height: 365px;
    background: linear-gradient(160deg, #6a8de2 0%, #8fa8e6 40%, #d9d4e8 70%, #6f9f8e 100%);
  }

  .values-card {
    position: absolute; left: 300px; top: 108px; width: 270px; height: 640px;
    background: var(--panel-white); border-radius: 20px 20px 0 0; overflow: hidden;
  }
  .section { position: absolute; left: 0; width: 270px; }
  .section.vision { top: 0; height: 283px; }
  .section.mission { top: 283px; height: 145px; background: var(--panel-grey); }
  .section.values { top: 428px; height: 212px; background: var(--panel-light); }
  .section-head { position: absolute; left: 0; top: 25px; height: 25px; display: flex; align-items: center; }
  .head-band { height: 25px; width: 75px; border-radius: 0 13px 13px 0; display: flex; align-items: center; justify-content: flex-end; padding-right: 12px; }
  .vision .head-band { background: var(--brand-teal); }
  .mission .head-band { background: var(--brand-lime); }
  .values .head-band { background: var(--soft-teal); margin-left: 15px; width: 60px; }
  .head-band svg { width: 26px; height: 20px; }
  .section-title { margin-left: 12px; color: var(--heading-blue); font-weight: 600; font-size: 15px; letter-spacing: 0.2px; }
  .section-body { position: absolute; left: 38px; width: 214px; color: var(--body-grey); font-size: 9.4px; line-height: 1.24; text-align: justify; }
  .vision .section-body { top: 60px; }
  .mission .section-body { top: 60px; }
  .values .section-body { top: 62px; }
  .section-body p + p { margin-top: 11px; }

  .footer {
    position: absolute; left: 0; top: 748px; width: 576px; height: 65px;
    background: var(--brand-teal); color: #fff;
    font-weight: 700; font-size: 14px; letter-spacing: 2px; text-align: center; line-height: 58px;
  }
</style>
</head>
<body>
  <main class="poster">
    <header class="headline">
      <div class="line-lg">RISING ABOVE</div>
      <div class="line-sm">THE COMPLEXITY OF</div>
      <div class="word-health">HEALTH</div>
      <div class="word-care">CARE</div>
    </header>

    <div class="brand">
      <span class="brand-dot"></span>
      <div class="brand-name">CareWillow</div>
    </div>

    <div class="who-tag">WHO WE ARE</div>
    <p class="who-text">We are friendly, servant leaders who have a sense of urgency to meet the needs of our nurses and clients. We prioritize personal relationships with genuine caring and compassion. We inspire others through our passion and energy.</p>

    <div class="photo" role="img" aria-label="Photograph of a smiling nurse in green scrubs helping an elderly man walk with a walker"></div>

    <section class="values-card">
      <div class="section vision">
        <div class="section-head">
          <div class="head-band">
            <svg viewBox="0 0 26 20" aria-hidden="true"><ellipse cx="13" cy="10" rx="12" ry="7" fill="#1d2a2a"/><circle cx="13" cy="10" r="4.5" fill="#fff"/><circle cx="13" cy="10" r="2.5" fill="#1d2a2a"/></svg>
          </div>
          <h2 class="section-title">OUR VISION</h2>
        </div>
        <div class="section-body">
          <p>We are transforming the healthcare staffing and homecare industry with our people-oriented, world-class team.</p>
          <p>Clients choose us, and develop lasting bonds with our team because of our impeccably high standards and our reputation for always remembering this is, first and foremost, a people business.</p>
          <p>We consistently go the extra mile to ensure our nurses and those being cared for are at all times, treated with dignity and respect. We hold ourselves and those we work with to the highest possible standards.</p>
          <p>We consistently deliver what we promise, and whenever possible, even more.</p>
        </div>
      </div>

      <div class="section mission">
        <div class="section-head">
          <div class="head-band">
            <svg viewBox="0 0 26 20" aria-hidden="true"><circle cx="12" cy="10" r="8" fill="none" stroke="#2f3b2a" stroke-width="1.6"/><circle cx="12" cy="10" r="4.5" fill="none" stroke="#2f3b2a" stroke-width="1.6"/><circle cx="12" cy="10" r="1.5" fill="#2f3b2a"/><path d="M12 10 L24 4" stroke="#2f3b2a" stroke-width="1.6"/></svg>
          </div>
          <h2 class="section-title">OUR MISSION</h2>
        </div>
        <div class="section-body">
          <p>We go above and beyond to ensure our clients receive the right care and the right people at the right time. Our rigorous recruitment standards result in strong caregivers who are trusted for their expertise, experience and compassion</p>
        </div>
      </div>

      <div class="section values">
        <div class="section-head">
          <div class="head-band">
            <svg viewBox="0 0 26 20" aria-hidden="true"><path d="M3 13 Q8 10 13 13 L21 11 Q24 11 23 14 L14 18 L3 17 Z" fill="none" stroke="#2f3b3a" stroke-width="1.5"/><path d="M13 9 C9 6 10 2 13 4 C16 2 17 6 13 9 Z" fill="#2f3b3a"/></svg>
          </div>
          <h2 class="section-title">OUR VALUES</h2>
        </div>
        <div class="section-body">
          <p>Through our genuine caring and compassion, we are committed to honor all with whom we interact. We are grounded in our faith and dedicated to working together as a family that consistently and passionately lives our values.</p>
          <p>Compassion Integrity and honesty Faith Decisive action Constant and never-ending improvement Personal ownership Excellence Positive attitude Passion Respect.</p>
        </div>
      </div>
    </section>

    <footer class="footer">www.carewillow.com</footer>
  </main>
</body>
</html>
```